Vantrel Grace Dental offce
Professional
Jessa
Owner
2871 Fenwick Ln
Coopersburg, Pa
jessakweldon@mailbrook.com
I uploaded my logo on the intro page
Please let me know if there are any problems. 610-824-3917 or jessakweldon@mailbrook.com

```html
<!DOCTYPE html>
<html lang="en">
<head>
<meta charset="utf-8">
<title>Vantrel Grace Dental offce – Stationery Set</title>
<link href="https://fonts.googleapis.com/css2?family=Montserrat:wght@400;600&display=swap" rel="stylesheet">
<style>
  :root {
    --bg: #e9dcc6;
    --paper: #ffffff;
    --blue: #2c5a9c;
    --orange: #f08a24;
    --ink: #5d6b7a;
    --label: #6f5a40;
    --brand: #2c5a9c;
    --crease: #e4e4e4;
  }
  * { margin: 0; padding: 0; box-sizing: border-box; }
  html, body { width: 1200px; height: 446px; overflow: hidden; }
  body {
    background: var(--bg);
    font-family: "Montserrat", sans-serif;
    position: relative;
  }
  .piece {
    position: absolute;
    background: var(--paper);
    box-shadow: 0 1px 3px rgba(0,0,0,.18);
    overflow: hidden;
  }
  .piece svg.art { position: absolute; inset: 0; width: 100%; height: 100%; }
  .label {
    position: absolute;
    font-size: 6px;
    letter-spacing: .6px;
    text-transform: uppercase;
    color: var(--label);
    white-space: nowrap;
  }
  .brand {
    position: absolute;
    display: flex;
    align-items: center;
    gap: 4px;
    color: var(--brand);
    font-weight: 600;
    text-transform: uppercase;
    white-space: nowrap;
  }
  .brand .dot { border-radius: 50%; background: var(--orange); flex: none; }
  .contact {
    position: absolute;
    font-size: 4.5px;
    line-height: 7px;
    color: var(--ink);
    white-space: nowrap;
  }

  /* Business cards */
  .card { width: 106px; height: 46px; left: 19px; }
  .card-front { top: 220px; }
  .card-back { top: 290px; }
  .card .brand { font-size: 3.4px; gap: 2px; left: 6px; top: 7px; }
  .card .brand .dot { width: 5px; height: 5px; }
  .card .contact { left: 6px; top: 22px; font-size: 3.4px; line-height: 5px; }
  .card-back .brand { left: 18px; top: 20px; }

  /* Letterheads */
  .letterhead { width: 305px; height: 389px; top: 19px; }
  .letterhead-one { left: 151px; }
  .letterhead-two { left: 473px; }
  .letterhead .brand { font-size: 7px; left: 22px; top: 22px; }
  .letterhead .brand .dot { width: 12px; height: 12px; }
  .letterhead-one .contact { left: 22px; bottom: 24px; }
  .letterhead-two .contact { left: 0; right: 0; bottom: 22px; text-align: center; }

  /* Envelopes */
  .envelope { left: 840px; width: 336px; }
  .envelope-blue { top: 19px; height: 72px; }
  .envelope-orange { top: 96px; height: 80px; }
  .envelope-plain { top: 181px; height: 66px; }
  .envelope-dl { left: 792px; top: 262px; width: 360px; height: 100px; }
  .envelope-dl .brand { font-size: 7px; left: 18px; top: 14px; }
  .envelope-dl .brand .dot { width: 11px; height: 11px; }
  .envelope-dl .contact { left: 18px; top: 34px; }
</style>
</head>
<body>
  <div class="label" style="left:19px; top:198px;">Stationery Concepts</div>

  <div class="piece card card-front">
    <svg class="art" viewBox="0 0 106 46" preserveAspectRatio="none" aria-hidden="true">
      <path d="M66 0 H106 V12 Q86 8 66 0 Z" fill="var(--blue)"/>
      <path d="M60 0 Q84 12 106 16" stroke="var(--orange)" stroke-width="1.5" fill="none"/>
    </svg>
    <div class="brand"><span class="dot"></span>Vantrel Grace Dental offce</div>
    <div class="contact">Jessa, Owner<br>610-824-3917<br>jessakweldon@mailbrook.com</div>
  </div>
  <div class="label" style="left:19px; top:270px;">Business Card Front</div>

  <div class="piece card card-back">
    <svg class="art" viewBox="0 0 106 46" preserveAspectRatio="none" aria-hidden="true">
      <path d="M0 46 H44 Q22 39 0 36 Z" fill="var(--blue)"/>
      <path d="M0 32 Q28 37 52 46" stroke="var(--orange)" stroke-width="1.5" fill="none"/>
    </svg>
    <div class="brand"><span class="dot"></span>Vantrel Grace Dental offce</div>
  </div>
  <div class="label" style="left:19px; top:340px;">Business Card Back</div>

  <div class="piece letterhead letterhead-one">
    <svg class="art" viewBox="0 0 305 389" preserveAspectRatio="none" aria-hidden="true">
      <path d="M150 0 H305 V42 Q225 30 150 0 Z" fill="var(--blue)"/>
      <path d="M140 0 Q220 40 305 52" stroke="var(--orange)" stroke-width="5" fill="none"/>
      <path d="M230 389 Q270 370 305 362 V389 Z" fill="var(--blue)"/>
      <path d="M215 389 Q262 364 305 356" stroke="var(--orange)" stroke-width="3" fill="none"/>
    </svg>
    <div class="brand"><span class="dot"></span>Vantrel Grace Dental offce</div>
    <div class="contact">2871 Fenwick Ln, Coopersburg, Pa<br>610-824-3917<br>jessakweldon@mailbrook.com</div>
  </div>
  <div class="label" style="left:260px; top:414px;">Letter Head Option 1</div>

  <div class="piece letterhead letterhead-two">
    <svg class="art" viewBox="0 0 305 389" preserveAspectRatio="none" aria-hidden="true">
      <path d="M150 0 H305 V42 Q225 30 150 0 Z" fill="var(--blue)"/>
      <path d="M140 0 Q220 40 305 52" stroke="var(--orange)" stroke-width="5" fill="none"/>
      <line x1="30" y1="355" x2="275" y2="355" stroke="var(--orange)" stroke-width="1"/>
    </svg>
    <div class="brand"><span class="dot"></span>Vantrel Grace Dental offce</div>
    <div class="contact">2871 Fenwick Ln, Coopersburg, Pa &nbsp;·&nbsp; 610-824-3917 &nbsp;·&nbsp; jessakweldon@mailbrook.com</div>
  </div>
  <div class="label" style="left:582px; top:414px;">Letter Head Option 2</div>

  <div class="piece envelope envelope-blue">
    <svg class="art" viewBox="0 0 336 72" preserveAspectRatio="none" aria-hidden="true">
      <rect x="0" y="0" width="336" height="62" fill="var(--blue)"/>
    </svg>
  </div>

  <div class="piece envelope envelope-orange">
    <svg class="art" viewBox="0 0 336 80" preserveAspectRatio="none" aria-hidden="true">
      <path d="M0 0 H336 V40 H300 L168 24 L36 40 H0 Z" fill="var(--orange)"/>
      <path d="M0 80 L168 48 L336 80" stroke="var(--crease)" stroke-width="1" fill="none"/>
    </svg>
  </div>

  <div class="piece envelope envelope-plain">
    <svg class="art" viewBox="0 0 336 66" preserveAspectRatio="none" aria-hidden="true">
      <path d="M0 0 L168 40 L336 0" stroke="var(--crease)" stroke-width="1" fill="none"/>
      <path d="M0 66 L140 30 M336 66 L196 30" stroke="var(--crease)" stroke-width="1" fill="none"/>
    </svg>
  </div>

  <div class="piece envelope-dl">
    <svg class="art" viewBox="0 0 360 100" preserveAspectRatio="none" aria-hidden="true">
      <path d="M275 100 Q318 84 360 80 V100 Z" fill="var(--blue)"/>
      <path d="M255 100 Q308 76 360 72" stroke="var(--orange)" stroke-width="3" fill="none"/>
    </svg>
    <div class="brand"><span class="dot"></span>Vantrel Grace Dental offce</div>
    <div class="contact">2871 Fenwick Ln<br>Coopersburg, Pa</div>
  </div>
  <div class="label" style="left:935px; top:368px;">Envelope Option 1</div>
</body>
</html>
```